Outpost Lattice Advisors – Franchise Growth & Development Presentation

Outpost Lattice Advisors is an outsourced franchise sales organization (FSO) that helps franchisors grow their franchise systems without the expense and risk of hiring an internal franchise development team.

We are seeking a professional PowerPoint presentation that will be used to present our services to franchisors, franchise executives, founders, and growth-stage franchise brands.

The presentation should communicate the value of partnering with Outpost Lattice Advisors, including:

• Fractional franchise sales team versus hiring internal staff
• 30+ years of franchise industry experience
• 550+ franchise sales successes
• Immediate access to established franchise broker relationships
• Proven franchise development processes
• Franchise growth strategy and enterprise value creation
• Potential private equity and exit opportunities through franchise expansion

The presentation should feel like a modern consulting, investment, or growth strategy presentation rather than a typical sales brochure. We want strong visual storytelling, custom infographics, professional diagrams, and clean business-oriented design.

The audience includes business owners, franchise founders, franchise executives, and investors who are evaluating growth strategies for their franchise systems.

Target Market(s)

Primary Audience: Emerging franchisors Growth-stage franchise brands Franchise founders Franchise CEOs Franchise presidents Franchise development executives Secondary Audience: Private equity firms Franchise investors Strategic buyers Franchise consultants

Industry/Entity Type

Franchise Development, Private Equity / Business Expansion

Font styles to use
Other font styles liked:
• Use Montserrat for titles and Open Sans for body text.

Requirements
Must have
• Modern professional business design Consistent branding throughout Custom infographics Comparison graphics Broker network ecosystem graphic Enterprise value graphic Easy-to-read charts and visuals Editable PowerPoint format Professional iconography. www.outpostlatticeadvisors.example as reference for colors
Nice to have
• Franchise-related imagery Subtle growth-themed visuals Timeline graphics Data visualization Private equity / valuation style graphics
Should not have
• Cartoon graphics Clip art Overly busy slides Stock-template appearance Bright neon colors Handwritten fonts Excessive text on slides Juvenile or playful design elements

```html
<!DOCTYPE html>
<html lang="en">
<head>
<meta charset="utf-8">
<title>How We Work Together – Outpost Lattice Advisors</title>
<link href="https://fonts.googleapis.com/css2?family=Montserrat:wght@600;700&family=Open+Sans:wght@400;700&display=swap" rel="stylesheet">
<style>
:root{
  --bg:#f5f6fa;
  --navy:#141f3b;
  --gold:#b08a3e;
  --body:#5d6677;
  --line:#dde1ea;
  --footer:#5f6b80;
}
*{margin:0;padding:0;box-sizing:border-box}
html,body{width:1200px;height:675px;overflow:hidden;background:var(--bg)}
.slide{position:relative;width:1200px;height:675px;background:var(--bg);font-family:"Open Sans",Arial,sans-serif}
.eyebrow{position:absolute;left:55px;top:45px;font-family:"Open Sans",Arial,sans-serif;font-weight:700;font-size:15.5px;letter-spacing:2.6px;color:var(--gold)}
.title{position:absolute;left:54px;top:76px;width:620px;font-family:"Montserrat",Arial,sans-serif;font-weight:700;font-size:34px;line-height:36px;color:var(--navy)}
.connector{position:absolute;left:178px;top:274px;width:853px;height:2px;background:var(--line)}
.step{position:absolute;top:234px;width:280px;text-align:center}
.step-icon{position:relative;width:82px;height:82px;margin:0 auto;border-radius:50%;background:var(--navy);box-shadow:0 5px 12px rgba(20,31,59,.18);display:flex;align-items:center;justify-content:center}
.step-num{position:absolute;right:-14px;top:-13px;width:33px;height:33px;border-radius:50%;background:var(--bg);border:2px solid var(--gold);color:var(--gold);font-family:"Montserrat",Arial,sans-serif;font-weight:700;font-size:14px;line-height:29px;text-align:center}
.step-title{margin-top:30px;font-family:"Montserrat",Arial,sans-serif;font-weight:700;font-size:16.5px;color:var(--navy)}
.step-text{margin:38px auto 0;width:250px;font-size:12.5px;line-height:18px;color:var(--body)}
.footer-brand{position:absolute;left:45px;top:651px;font-size:10.5px;letter-spacing:2px;color:var(--footer)}
.page-num{position:absolute;right:39px;top:651px;font-size:10.5px;color:var(--footer)}
</style>
</head>
<body>
<div class="slide">
  <div class="eyebrow">HOW WE WORK TOGETHER</div>
  <h1 class="title">A Simple, Structured Path to Getting Started</h1>

  <div class="connector"></div>

  <div class="step" style="left:42px">
    <div class="step-icon"><span class="step-num">1</span>
      <svg width="40" height="40" viewBox="0 0 24 24"><path fill="#fff" d="M6.6 10.8a15.1 15.1 0 0 0 6.6 6.6l2.2-2.2c.3-.3.7-.4 1-.2 1.1.4 2.3.6 3.6.6.6 0 1 .4 1 1V20c0 .6-.4 1-1 1A17 17 0 0 1 3 4c0-.6.4-1 1-1h3.5c.6 0 1 .4 1 1 0 1.3.2 2.5.6 3.6.1.3 0 .7-.2 1z"/></svg>
    </div>
    <div class="step-title">Strategy Call</div>
    <p class="step-text">We learn about your brand, goals, and current development gaps.</p>
  </div>

  <div class="step" style="left:325px">
    <div class="step-icon"><span class="step-num">2</span>
      <svg width="40" height="40" viewBox="0 0 24 24" fill="#fff"><rect x="9.5" y="3" width="5" height="4.5" rx="1"/><rect x="3" y="15" width="5" height="4.5" rx="1"/><rect x="9.5" y="15" width="5" height="4.5" rx="1"/><rect x="16" y="15" width="5" height="4.5" rx="1"/><path d="M11.3 7.5h1.4v3.2h6.3V15h-1.4v-2.9H6.4V15H5v-4.3h6.3z"/><rect x="11.3" y="10.7" width="1.4" height="4.3"/></svg>
    </div>
    <div class="step-title">Custom Growth Plan</div>
    <p class="step-text">We design a fractional development plan tailored to your system.</p>
  </div>

  <div class="step" style="left:600px">
    <div class="step-icon"><span class="step-num">3</span>
      <svg width="42" height="42" viewBox="0 0 24 24" fill="#fff"><circle cx="12" cy="8" r="3.2"/><circle cx="5.5" cy="9.5" r="2.2"/><circle cx="18.5" cy="9.5" r="2.2"/><path d="M6.5 18.5c0-3 2.5-5.2 5.5-5.2s5.5 2.2 5.5 5.2z"/><path d="M1.5 17c0-2 1.6-3.5 3.8-3.5.7 0 1.3.1 1.8.4A6.4 6.4 0 0 0 5.4 17z"/><path d="M22.5 17c0-2-1.6-3.5-3.8-3.5-.7 0-1.3.1-1.8.4a6.4 6.4 0 0 1 1.7 3.1z"/></svg>
    </div>
    <div class="step-title">Embedded Team Launch</div>
    <p class="step-text">Our team activates broker channels, lead generation, and sales processes.</p>
  </div>

  <div class="step" style="left:893px">
    <div class="step-icon"><span class="step-num">4</span>
      <svg width="38" height="38" viewBox="0 0 24 24"><path d="M12 20V5M5 11.5 12 4.5l7 7" fill="none" stroke="#fff" stroke-width="3" stroke-linecap="round" stroke-linejoin="round"/></svg>
    </div>
    <div class="step-title">Ongoing Optimization</div>
    <p class="step-text">We report on performance and continuously refine your growth strategy.</p>
  </div>

  <div class="footer-brand">OUTPOST LATTICE ADVISORS</div>
  <div class="page-num">10</div>
</div>
</body>
</html>
```